Now Open Poster

We need a banner for our sports supplement and nutritional store, Harbor Nutrition.
We were hoping for some sort of creative word art piece.
I have drawn my own mock up just to give you all a very basic starting point. But you are free to go with whatever you feel will work best.
The primary objective is simply to explain a little about what the company does, and then direct traffic towards the store with an 'Open Arrow' pointing left.
Text words we have chosen are:
Protein
Creatine
Health
Fitness
Sports Science
Nutrition
Energy
Achievement
Amino Acids
Organic
Supplements
Performance
Testosterone Support
Vitamins
Growth
Diet
Happiness
Weight Loss
Strong
Natural
Vitality
Accomplished
Below the word art we want our logo (See attached options)
Then below the logo the phrase "Success Starts Here"
Dimensions of the poster are 140cm x 60cm.
Colours: Blues/Whites/Greys/Blacks (Lots of white space please)
Here are some cool pieces I found that had some interesting elements that I liked (I'd love to see a mash-up of styles with a street art feel to it. Something funky!):
http://www.moodwall-example.com/pin/100000000000000001/
http://www.moodwall-example.com/pin/100000000000000002/
http://www.moodwall-example.com/pin/100000000000000003/
http://www.moodwall-example.com/pin/100000000000000004/
http://www.moodwall-example.com/pin/100000000000000005/
Thanks for reading, message me if you have any further questions!
- Tobias

```html
<!DOCTYPE html>
<html lang="en">
<head>
<meta charset="utf-8">
<title>Harbor Nutrition – Now Open Banner</title>
<link rel="stylesheet" href="https://fonts.googleapis.com/css2?family=Montserrat:wght@500;800;900&family=Oswald:wght@300;400;500;600&family=Six+Caps&family=Michroma&display=swap">
<style>
  :root{
    --board-top:#d6d6d8;
    --board-bottom:#f3f3f4;
    --divider:#b9b9bc;
  }
  html,body{margin:0;padding:0;overflow:hidden;}
  body{width:1200px;height:1000px;position:relative;
    background:linear-gradient(180deg,var(--board-top) 0%,var(--board-bottom) 45%,#ececed 100%);
    font-family:"Montserrat",sans-serif;}
  .divider{position:absolute;left:608px;top:53px;width:1px;height:896px;background:var(--divider);}

  /* ---------- banner ---------- */
  .banner{position:absolute;width:384px;height:896px;overflow:hidden;box-sizing:border-box;
    background:var(--bg);color:var(--ink);
    --bg:#000;--ink:#fff;}
  .banner--main{left:133px;top:53px;}
  .banner--mini{transform:scale(.4948);transform-origin:0 0;}
  .banner--slate{left:697px;top:53px;}
  .banner--sky{left:909px;top:53px;}
  .banner--paper{left:697px;top:505px;border:4px solid #000;border-radius:8px;}
  .banner--paper > *{margin-left:-4px;margin-top:-4px;}
  .banner--olive{left:909px;top:505px;}

  .banner--slate{--bg:#6d6e71;--ink:#fff;
    --w-protein:#d9d9d9;--w-fitness:#1b1b1b;--w-health:#1e2f5c;--w-science:#9cc3e4;--w-energy:#a8a8ab;
    --w-nutrition:#151515;--w-loss:#1e2f5c;--w-happiness:#9cc3e4;--w-strong:#9cc3e4;--w-natural:#5fd0ee;
    --w-amino:#151515;--w-achievement:#151515;--w-performance:#5fd0ee;--w-organic:#1e2f5c;
    --w-supplements:#3e5b8c;--w-vitality:#1e2f5c;--w-cap:#d9d9d9;}
  .banner--sky{--bg:#1ea5cf;--ink:#fff;
    --w-protein:#d9d9d9;--w-fitness:#1b2a4a;--w-health:#1b2a4a;--w-science:#8cd0ea;--w-energy:#1b6f93;
    --w-nutrition:#151a24;--w-loss:#1b2a4a;--w-happiness:#8cd0ea;--w-strong:#1b6f93;--w-natural:#8cd0ea;
    --w-amino:#1b2a4a;--w-achievement:#151a24;--w-performance:#8cd0ea;--w-organic:#1b6f93;
    --w-supplements:#1b6f93;--w-vitality:#1b2a4a;--w-cap:#d9d9d9;}
  .banner--paper{--bg:#fff;--ink:#111;}
  .banner--olive{--bg:#3e4238;--ink:#fff;
    --w-protein:#7bc043;--w-fitness:#2fb7d6;--w-sports:#9b4fa8;--w-health:#f28c28;--w-creatine:#2fb7d6;
    --w-science:#2a2c27;--w-energy:#7bc043;--w-growth:#f28c28;--w-nutrition:#222;--w-diet:#7bc043;
    --w-weight:#9b4fa8;--w-loss:#7bc043;--w-happiness:#f28c28;--w-strong:#2fb7d6;--w-natural:#e52b6f;
    --w-amino:#222;--w-achievement:#222;--w-vitamins:#222;--w-performance:#e52b6f;--w-testosterone:#222;
    --w-organic:#f28c28;--w-supplements:#7bc043;--w-vitality:#9b4fa8;--w-cap:#2a2c27;--w-ccomplishe:#222;}

  /* open header */
  .open-row{position:absolute;left:0;top:41px;width:384px;height:28px;display:flex;justify-content:center;align-items:center;gap:17px;}
  .open-row svg{width:68px;height:24px;fill:var(--ink);flex:none;}
  .open-label{font-family:"Michroma",sans-serif;font-weight:700;font-size:28px;letter-spacing:5px;line-height:1;color:var(--ink);}

  /* word cloud */
  .word{position:absolute;line-height:1;white-space:nowrap;margin:0;
    transform:scaleX(var(--sx,1));transform-origin:0 0;}
  .w-protein{left:40px;top:96px;font:800 36px/1 "Montserrat",sans-serif;color:var(--w-protein,var(--ink));}
  .w-fitness{left:230px;top:96px;font:300 40px/1 "Oswald",sans-serif;letter-spacing:1px;--sx:.95;color:var(--w-fitness,var(--ink));}
  .w-sports{left:41px;top:144px;font:400 100px/1 "Six Caps",sans-serif;--sx:.85;color:var(--w-sports,var(--ink));}
  .w-health{left:172px;top:138px;font:300 85px/1 "Oswald",sans-serif;--sx:.84;color:var(--w-health,var(--ink));}
  .w-creatine{left:40px;top:248px;font:400 44px/1 "Oswald",sans-serif;--sx:.74;color:var(--w-creatine,var(--ink));}
  .w-science{left:174px;top:228px;font:400 66px/1 "Six Caps",sans-serif;--sx:.85;color:var(--w-science,var(--ink));}
  .w-energy{left:280px;top:231px;font:400 22px/1 "Oswald",sans-serif;--sx:.95;color:var(--w-energy,var(--ink));}
  .w-growth{left:280px;top:257px;font:300 32px/1 "Oswald",sans-serif;--sx:.68;color:var(--w-growth,var(--ink));}
  .w-nutrition{left:41px;top:299px;font:800 38px/1 "Montserrat",sans-serif;color:var(--w-nutrition,var(--ink));}
  .w-diet{left:280px;top:299px;font:300 40px/1 "Oswald",sans-serif;letter-spacing:4px;--sx:.95;color:var(--w-diet,var(--ink));}
  .w-weight{left:40px;top:348px;font:400 28px/1 "Oswald",sans-serif;--sx:.78;color:var(--w-weight,var(--ink));}
  .w-loss{left:41px;top:377px;font:400 49px/1 "Oswald",sans-serif;--sx:.7;color:var(--w-loss,var(--ink));}
  .w-happiness{left:117px;top:345px;font:400 85px/1 "Six Caps",sans-serif;--sx:.78;color:var(--w-happiness,var(--ink));}
  .w-strong{left:280px;top:348px;font:400 31px/1 "Oswald",sans-serif;--sx:.72;color:var(--w-strong,var(--ink));}
  .w-natural{left:280px;top:393px;font:600 31px/1 "Oswald",sans-serif;--sx:.6;color:var(--w-natural,var(--ink));}
  .w-amino{left:40px;top:436px;font:400 30px/1 "Six Caps",sans-serif;--sx:.8;color:var(--w-amino,var(--ink));}
  .w-achievement{left:120px;top:435px;font:500 31px/1 "Oswald",sans-serif;--sx:.85;color:var(--w-achievement,var(--ink));}
  .w-vitamins{left:280px;top:435px;font:300 31px/1 "Oswald",sans-serif;--sx:.66;color:var(--w-vitamins,var(--ink));}
  .w-performance{left:40px;top:476px;font:800 16px/1 "Montserrat",sans-serif;color:var(--w-performance,var(--ink));}
  .w-testosterone{left:194px;top:479px;font:400 15px/1 "Oswald",sans-serif;letter-spacing:.6px;--sx:.95;color:var(--w-testosterone,var(--ink));}
  .w-organic{left:39px;top:505px;font:400 41px/1 "Six Caps",sans-serif;--sx:.95;color:var(--w-organic,var(--ink));}
  .w-supplements{left:120px;top:503px;font:500 44px/1 "Oswald",sans-serif;--sx:.9;color:var(--w-supplements,var(--ink));}
  .w-cap-a{left:35px;top:552px;font:900 84px/1 "Montserrat",sans-serif;color:var(--w-cap,var(--ink));}
  .w-cap-d{left:294px;top:552px;font:900 84px/1 "Montserrat",sans-serif;color:var(--w-cap,var(--ink));}
  .w-vitality{left:122px;top:556px;font:300 31px/1 "Oswald",sans-serif;letter-spacing:5px;--sx:.95;color:var(--w-vitality,var(--ink));}
  .w-ccomplishe{left:100px;top:589px;font:800 36px/1 "Montserrat",sans-serif;--sx:.76;color:var(--w-ccomplishe,var(--ink));}
  .flag{position:absolute;top:562px;width:14px;height:22px;fill:var(--w-vitality,var(--ink));}
  .flag--left{left:100px;}
  .flag--right{left:272px;}

  /* brand mark */
  .brand{position:absolute;left:122px;top:652px;width:140px;height:140px;box-sizing:border-box;
    border:2px solid var(--ink);border-radius:50%;display:flex;flex-direction:column;justify-content:center;align-items:center;
    font-family:"Michroma",sans-serif;font-size:12px;letter-spacing:1px;line-height:1.6;color:var(--ink);}

  /* tagline */
  .tagline{position:absolute;left:0;top:812px;width:384px;text-align:center;margin:0;
    font-family:"Michroma",sans-serif;font-size:15px;letter-spacing:4px;line-height:30px;color:var(--ink);}
</style>
</head>
<body>

<div class="divider"></div>

<section class="banner banner--main" aria-label="Harbor Nutrition now open banner, black">
  <div class="open-row">
    <svg viewBox="0 0 68 24" aria-hidden="true"><polygon points="11,0 22,0 11,12 22,24 11,24 0,12"/><polygon points="34,0 45,0 34,12 45,24 34,24 23,12"/><polygon points="57,0 68,0 57,12 68,24 57,24 46,12"/></svg>
    <span class="open-label">OPEN</span>
    <svg viewBox="0 0 68 24" aria-hidden="true"><polygon points="11,0 22,0 11,12 22,24 11,24 0,12"/><polygon points="34,0 45,0 34,12 45,24 34,24 23,12"/><polygon points="57,0 68,0 57,12 68,24 57,24 46,12"/></svg>
  </div>
  <p class="word w-protein">PROTEIN</p><p class="word w-fitness">FITNESS</p>
  <p class="word w-sports">SPORTS</p><p class="word w-health">HEALTH</p>
  <p class="word w-creatine">CREATINE</p><p class="word w-science">SCIENCE</p>
  <p class="word w-energy">ENERGY</p><p class="word w-growth">GROWTH</p>
  <p class="word w-nutrition">NUTRITION</p><p class="word w-diet">DIET</p>
  <p class="word w-weight">WEIGHT</p><p class="word w-loss">LOSS</p>
  <p class="word w-happiness">HAPPINESS</p>
  <p class="word w-strong">STRONG</p><p class="word w-natural">NATURAL</p>
  <p class="word w-amino">AMINO ACIDS</p><p class="word w-achievement">ACHIEVEMENT</p><p class="word w-vitamins">VITAMINS</p>
  <p class="word w-performance">PERFORMANCE</p><p class="word w-testosterone">TESTOSTERONE SUPPORT</p>
  <p class="word w-organic">ORGANIC</p><p class="word w-supplements">SUPPLEMENTS</p>
  <p class="word w-cap-a">A</p>
  <svg class="flag flag--left" viewBox="0 0 14 22" aria-hidden="true"><polygon points="0,0 14,0 14,22 0,22 6,11"/></svg>
  <p class="word w-vitality">VITALITY</p>
  <svg class="flag flag--right" viewBox="0 0 14 22" aria-hidden="true"><polygon points="0,0 14,0 8,11 14,22 0,22"/></svg>
  <p class="word w-ccomplishe">CCOMPLISHE</p>
  <p class="word w-cap-d">D</p>
  <div class="brand"><span>HARBOR</span><span>NUTRITION</span></div>
  <p class="tagline">SUCCESS STARTS<br>HERE.</p>
</section>

<section class="banner banner--mini banner--slate" aria-label="Banner colourway, slate grey">
  <div class="open-row">
    <svg viewBox="0 0 68 24" aria-hidden="true"><polygon points="11,0 22,0 11,12 22,24 11,24 0,12"/><polygon points="34,0 45,0 34,12 45,24 34,24 23,12"/><polygon points="57,0 68,0 57,12 68,24 57,24 46,12"/></svg>
    <span class="open-label">OPEN</span>
    <svg viewBox="0 0 68 24" aria-hidden="true"><polygon points="11,0 22,0 11,12 22,24 11,24 0,12"/><polygon points="34,0 45,0 34,12 45,24 34,24 23,12"/><polygon points="57,0 68,0 57,12 68,24 57,24 46,12"/></svg>
  </div>
  <p class="word w-protein">PROTEIN</p><p class="word w-fitness">FITNESS</p>
  <p class="word w-sports">SPORTS</p><p class="word w-health">HEALTH</p>
  <p class="word w-creatine">CREATINE</p><p class="word w-science">SCIENCE</p>
  <p class="word w-energy">ENERGY</p><p class="word w-growth">GROWTH</p>
  <p class="word w-nutrition">NUTRITION</p><p class="word w-diet">DIET</p>
  <p class="word w-weight">WEIGHT</p><p class="word w-loss">LOSS</p>
  <p class="word w-happiness">HAPPINESS</p>
  <p class="word w-strong">STRONG</p><p class="word w-natural">NATURAL</p>
  <p class="word w-amino">AMINO ACIDS</p><p class="word w-achievement">ACHIEVEMENT</p><p class="word w-vitamins">VITAMINS</p>
  <p class="word w-performance">PERFORMANCE</p><p class="word w-testosterone">TESTOSTERONE SUPPORT</p>
  <p class="word w-organic">ORGANIC</p><p class="word w-supplements">SUPPLEMENTS</p>
  <p class="word w-cap-a">A</p>
  <svg class="flag flag--left" viewBox="0 0 14 22" aria-hidden="true"><polygon points="0,0 14,0 14,22 0,22 6,11"/></svg>
  <p class="word w-vitality">VITALITY</p>
  <svg class="flag flag--right" viewBox="0 0 14 22" aria-hidden="true"><polygon points="0,0 14,0 8,11 14,22 0,22"/></svg>
  <p class="word w-ccomplishe">CCOMPLISHE</p>
  <p class="word w-cap-d">D</p>
  <div class="brand"><span>HARBOR</span><span>NUTRITION</span></div>
  <p class="tagline">SUCCESS STARTS<br>HERE.</p>
</section>

<section class="banner banner--mini banner--sky" aria-label="Banner colourway, sky blue">
  <div class="open-row">
    <svg viewBox="0 0 68 24" aria-hidden="true"><polygon points="11,0 22,0 11,12 22,24 11,24 0,12"/><polygon points="34,0 45,0 34,12 45,24 34,24 23,12"/><polygon points="57,0 68,0 57,12 68,24 57,24 46,12"/></svg>
    <span class="open-label">OPEN</span>
    <svg viewBox="0 0 68 24" aria-hidden="true"><polygon points="11,0 22,0 11,12 22,24 11,24 0,12"/><polygon points="34,0 45,0 34,12 45,24 34,24 23,12"/><polygon points="57,0 68,0 57,12 68,24 57,24 46,12"/></svg>
  </div>
  <p class="word w-protein">PROTEIN</p><p class="word w-fitness">FITNESS</p>
  <p class="word w-sports">SPORTS</p><p class="word w-health">HEALTH</p>
  <p class="word w-creatine">CREATINE</p><p class="word w-science">SCIENCE</p>
  <p class="word w-energy">ENERGY</p><p class="word w-growth">GROWTH</p>
  <p class="word w-nutrition">NUTRITION</p><p class="word w-diet">DIET</p>
  <p class="word w-weight">WEIGHT</p><p class="word w-loss">LOSS</p>
  <p class="word w-happiness">HAPPINESS</p>
  <p class="word w-strong">STRONG</p><p class="word w-natural">NATURAL</p>
  <p class="word w-amino">AMINO ACIDS</p><p class="word w-achievement">ACHIEVEMENT</p><p class="word w-vitamins">VITAMINS</p>
  <p class="word w-performance">PERFORMANCE</p><p class="word w-testosterone">TESTOSTERONE SUPPORT</p>
  <p class="word w-organic">ORGANIC</p><p class="word w-supplements">SUPPLEMENTS</p>
  <p class="word w-cap-a">A</p>
  <svg class="flag flag--left" viewBox="0 0 14 22" aria-hidden="true"><polygon points="0,0 14,0 14,22 0,22 6,11"/></svg>
  <p class="word w-vitality">VITALITY</p>
  <svg class="flag flag--right" viewBox="0 0 14 22" aria-hidden="true"><polygon points="0,0 14,0 8,11 14,22 0,22"/></svg>
  <p class="word w-ccomplishe">CCOMPLISHE</p>
  <p class="word w-cap-d">D</p>
  <div class="brand"><span>HARBOR</span><span>NUTRITION</span></div>
  <p class="tagline">SUCCESS STARTS<br>HERE.</p>
</section>

<section class="banner banner--mini banner--paper" aria-label="Banner colourway, white">
  <div class="open-row">
    <svg viewBox="0 0 68 24" aria-hidden="true"><polygon points="11,0 22,0 11,12 22,24 11,24 0,12"/><polygon points="34,0 45,0 34,12 45,24 34,24 23,12"/><polygon points="57,0 68,0 57,12 68,24 57,24 46,12"/></svg>
    <span class="open-label">OPEN</span>
    <svg viewBox="0 0 68 24" aria-hidden="true"><polygon points="11,0 22,0 11,12 22,24 11,24 0,12"/><polygon points="34,0 45,0 34,12 45,24 34,24 23,12"/><polygon points="57,0 68,0 57,12 68,24 57,24 46,12"/></svg>
  </div>
  <p class="word w-protein">PROTEIN</p><p class="word w-fitness">FITNESS</p>
  <p class="word w-sports">SPORTS</p><p class="word w-health">HEALTH</p>
  <p class="word w-creatine">CREATINE</p><p class="word w-science">SCIENCE</p>
  <p class="word w-energy">ENERGY</p><p class="word w-growth">GROWTH</p>
  <p class="word w-nutrition">NUTRITION</p><p class="word w-diet">DIET</p>
  <p class="word w-weight">WEIGHT</p><p class="word w-loss">LOSS</p>
  <p class="word w-happiness">HAPPINESS</p>
  <p class="word w-strong">STRONG</p><p class="word w-natural">NATURAL</p>
  <p class="word w-amino">AMINO ACIDS</p><p class="word w-achievement">ACHIEVEMENT</p><p class="word w-vitamins">VITAMINS</p>
  <p class="word w-performance">PERFORMANCE</p><p class="word w-testosterone">TESTOSTERONE SUPPORT</p>
  <p class="word w-organic">ORGANIC</p><p class="word w-supplements">SUPPLEMENTS</p>
  <p class="word w-cap-a">A</p>
  <svg class="flag flag--left" viewBox="0 0 14 22" aria-hidden="true"><polygon points="0,0 14,0 14,22 0,22 6,11"/></svg>
  <p class="word w-vitality">VITALITY</p>
  <svg class="flag flag--right" viewBox="0 0 14 22" aria-hidden="true"><polygon points="0,0 14,0 8,11 14,22 0,22"/></svg>
  <p class="word w-ccomplishe">CCOMPLISHE</p>
  <p class="word w-cap-d">D</p>
  <div class="brand"><span>HARBOR</span><span>NUTRITION</span></div>
  <p class="tagline">SUCCESS STARTS<br>HERE.</p>
</section>

<section class="banner banner--mini banner--olive" aria-label="Banner colourway, dark olive multicolour">
  <div class="open-row">
    <svg viewBox="0 0 68 24" aria-hidden="true"><polygon points="11,0 22,0 11,12 22,24 11,24 0,12"/><polygon points="34,0 45,0 34,12 45,24 34,24 23,12"/><polygon points="57,0 68,0 57,12 68,24 57,24 46,12"/></svg>
    <span class="open-label">OPEN</span>
    <svg viewBox="0 0 68 24" aria-hidden="true"><polygon points="11,0 22,0 11,12 22,24 11,24 0,12"/><polygon points="34,0 45,0 34,12 45,24 34,24 23,12"/><polygon points="57,0 68,0 57,12 68,24 57,24 46,12"/></svg>
  </div>
  <p class="word w-protein">PROTEIN</p><p class="word w-fitness">FITNESS</p>
  <p class="word w-sports">SPORTS</p><p class="word w-health">HEALTH</p>
  <p class="word w-creatine">CREATINE</p><p class="word w-science">SCIENCE</p>
  <p class="word w-energy">ENERGY</p><p class="word w-growth">GROWTH</p>
  <p class="word w-nutrition">NUTRITION</p><p class="word w-diet">DIET</p>
  <p class="word w-weight">WEIGHT</p><p class="word w-loss">LOSS</p>
  <p class="word w-happiness">HAPPINESS</p>
  <p class="word w-strong">STRONG</p><p class="word w-natural">NATURAL</p>
  <p class="word w-amino">AMINO ACIDS</p><p class="word w-achievement">ACHIEVEMENT</p><p class="word w-vitamins">VITAMINS</p>
  <p class="word w-performance">PERFORMANCE</p><p class="word w-testosterone">TESTOSTERONE SUPPORT</p>
  <p class="word w-organic">ORGANIC</p><p class="word w-supplements">SUPPLEMENTS</p>
  <p class="word w-cap-a">A</p>
  <svg class="flag flag--left" viewBox="0 0 14 22" aria-hidden="true"><polygon points="0,0 14,0 14,22 0,22 6,11"/></svg>
  <p class="word w-vitality">VITALITY</p>
  <svg class="flag flag--right" viewBox="0 0 14 22" aria-hidden="true"><polygon points="0,0 14,0 8,11 14,22 0,22"/></svg>
  <p class="word w-ccomplishe">CCOMPLISHE</p>
  <p class="word w-cap-d">D</p>
  <div class="brand"><span>HARBOR</span><span>NUTRITION</span></div>
  <p class="tagline">SUCCESS STARTS<br>HERE.</p>
</section>

</body>
</html>
```